HOLLOWPINE SPIRITS WEBSITE

HOLLOWPINE SPIRITS WHOLESALES ALCOHOL (WHISKY VODKA AND HELPS CREATES BOTTLING/BRANDING FOR PEOPLE WANTING LAUNCH THERE OWN BRANDS OF ALCOHOL

Colors

Designer to choose colors to be used in the design.

```html
<!DOCTYPE html>
<html lang="en">
<head>
<meta charset="utf-8">
<title>Hollowpine Spirits</title>
<link href="https://fonts.googleapis.com/css2?family=Michroma&family=Lato:wght@400;700&display=swap" rel="stylesheet">
<style>
:root{
  --gold:#ffc400;
  --ink:#0b0b0b;
  --panel:#1b1b1b;
  --text:#ffffff;
  --muted:#cfcfcf;
  --field:#262626;
}
*{box-sizing:border-box;margin:0;padding:0}
html,body{width:1200px;height:4751px;overflow:hidden;background:var(--ink)}
body{font-family:"Lato",sans-serif;color:var(--text);position:relative}
.head{font-family:"Michroma",sans-serif;font-weight:400;text-transform:uppercase}
section,footer{position:absolute;left:0;width:1200px;overflow:hidden}
.abs{position:absolute}
.btn{position:absolute;background:var(--gold);color:#fff;border-radius:30px;display:flex;align-items:center;justify-content:center;font-family:"Michroma",sans-serif;font-size:14px;text-transform:uppercase}
.title{position:absolute;left:0;width:1200px;text-align:center;font-size:31px}

/* hero */
.hero{top:0;height:799px}
.hero-photo{position:absolute;inset:0;background:radial-gradient(ellipse at 50% 60%,#c9862e 0%,#7a4214 30%,#3a1c09 60%,#140904 100%)}
.hero-shade{position:absolute;inset:0;background:linear-gradient(#000a,#0004 30%,#0006)}
.topbar-info{position:absolute;top:26px;display:flex;align-items:center;gap:12px;font-size:12.5px;line-height:18px}
.icon-dot{width:30px;height:30px;border-radius:50%;background:var(--gold);display:flex;align-items:center;justify-content:center;flex:none}
.brand{position:absolute;font-family:"Michroma",sans-serif;color:#fff;text-align:center;line-height:1}
.rule{position:absolute;left:111px;width:977px;height:1px;background:#ffffff66}
.nav{position:absolute;top:106px;left:0;width:1200px;display:flex;justify-content:center;gap:46px;font-size:12.5px;text-transform:uppercase}
.nav .on{color:var(--gold)}
.hero-welcome{position:absolute;top:232px;width:1200px;text-align:center;color:var(--gold);font-size:22px}
.hero-name{position:absolute;top:266px;width:1200px;text-align:center;font-size:52px;line-height:60px}
.hero-sub{position:absolute;top:335px;width:1200px;text-align:center;font-size:18px;letter-spacing:22px;color:var(--gold);padding-left:22px}
.hero-copy{position:absolute;top:378px;left:250px;width:700px;text-align:center;font-size:14.5px;line-height:26px}

/* about */
.about{top:799px;height:588px;background:var(--ink)}
.about h2{position:absolute;left:111px;top:88px;font-size:30px;line-height:44px}
.about-copy{position:absolute;left:111px;top:188px;width:450px;font-size:14.5px;line-height:26px}
.about-photo{position:absolute;left:645px;top:86px;width:443px;height:424px;border-radius:50%;background:radial-gradient(circle,#e09a2a 0%,#8a5212 35%,#2a1606 65%,#0b0b0b 72%);box-shadow:0 0 0 3px #b8862a inset}

/* wholesale */
.wholesale{top:1387px;height:774px;background:#121212}
.wholesale-copy{position:absolute;top:140px;left:160px;width:880px;text-align:center;font-size:14.5px;line-height:26px}
.tiles{position:absolute;left:111px;top:230px;width:977px;display:grid;grid-template-columns:repeat(3,313px);gap:21px 19px}
.tile{height:214px;display:flex;align-items:center;justify-content:center;font-weight:700;font-size:21px;text-transform:uppercase}

/* services */
.services{top:2161px;height:644px;background:radial-gradient(ellipse at 50% 40%,#3a3a3a,#1a1a1a 70%)}
.svc-floor{position:absolute;left:0;top:520px;width:1200px;height:124px;background:linear-gradient(#2a1a10,#4a2e1a)}
.svc-photo{position:absolute;left:420px;top:340px;width:360px;height:290px;background:radial-gradient(ellipse at 50% 70%,#5a3a1e,#0000 70%)}
.svc-icon{position:absolute;width:92px;height:92px;border-radius:50%;border:2px solid var(--gold);background:#111;display:flex;align-items:center;justify-content:center}
.svc{position:absolute;width:230px}
.svc h3{font-size:13px;margin-bottom:8px;white-space:nowrap}
.svc p{font-size:9px;line-height:15px;color:var(--muted)}
.svc a{display:block;margin-top:6px;color:var(--gold);font-family:"Michroma",sans-serif;font-size:8.5px}
.svc.r{text-align:right}

/* faq */
.faq{top:2805px;height:1018px;background:var(--ink)}
.faq-item{position:absolute;left:212px;width:802px;height:74px;border-radius:37px;background:var(--panel);display:flex;align-items:center}
.faq-num{width:60px;height:60px;margin-left:7px;border-radius:50%;background:#3a3a3a;display:flex;align-items:center;justify-content:center;font-family:"Michroma",sans-serif;font-size:22px;flex:none}
.faq-q{margin-left:26px;width:620px;font-size:15.5px;line-height:25px}
.faq-toggle{margin-left:auto;margin-right:30px;color:#888;font-size:24px}
.faq-item.open .faq-num{background:var(--gold)}
.faq-item.open .faq-toggle{color:var(--gold)}
.faq-answer{position:absolute;left:306px;top:598px;width:660px;padding-left:16px;border-left:2px solid var(--gold);font-size:14.5px;line-height:26px;color:var(--muted)}

/* contact */
.contact{top:3823px;height:529px;background:#121212}
.info{position:absolute;left:111px;display:flex;gap:20px}
.info-icon{width:50px;height:50px;border-radius:50%;border:2px solid #fff;display:flex;align-items:center;justify-content:center;flex:none}
.info h4{font-size:15px;margin-bottom:4px}
.info p{font-size:14px;line-height:22px;width:230px}
.field{position:absolute;width:318px;height:52px;background:var(--field);color:#999;font-size:14px;padding:14px 22px}

/* footer */
.footer{top:4352px;height:399px;background:var(--ink)}
.foot-h{position:absolute;top:50px;color:var(--gold);font-size:15px}
.foot-h::after{content:"";display:block;width:30px;height:2px;background:var(--gold);margin-top:10px}
.foot-list{position:absolute;top:103px;list-style:none;font-size:13.5px;line-height:30px}
.foot-line{position:absolute;left:845px;width:245px;height:1px;background:#777}
.copyright{position:absolute;top:4690px;left:0;width:1200px;text-align:center;font-size:14px}
</style>
</head>
<body>

<section class="hero">
  <div class="hero-photo" role="img" aria-label="Candle-lit cellar aisle lined with stacked oak barrels"></div>
  <div class="hero-shade"></div>
  <div class="topbar-info" style="left:114px">
    <span class="icon-dot"><svg width="14" height="16" viewBox="0 0 14 16"><path d="M7 1a5 5 0 0 1 5 5c0 4-5 9-5 9S2 10 2 6a5 5 0 0 1 5-5z" fill="#fff"/><circle cx="7" cy="6" r="2" fill="#ffc400"/></svg></span>
    <span>Hollowpine Spirits Building 12, Harbour<br>Lane 4, Eastmoor, 4821 KD</span>
  </div>
  <div class="brand" style="left:480px;top:26px;width:240px;font-size:21px">HOLLOWPINE<div style="font-size:9px;letter-spacing:6px;margin-top:6px">SPIRITS</div></div>
  <div class="topbar-info" style="left:800px;top:28px">
    <span class="icon-dot"><svg width="14" height="14" viewBox="0 0 14 14"><path d="M3 1l3 3-2 2c1 2 2 3 4 4l2-2 3 3-2 2C6 13 1 8 1 3z" fill="#fff"/></svg></span>
    <span>+31600000123</span>
  </div>
  <svg class="abs" style="left:985px;top:36px" width="14" height="14" viewBox="0 0 14 14"><circle cx="6" cy="6" r="4.5" stroke="#fff" stroke-width="2" fill="none"/><path d="M9.5 9.5L13 13" stroke="#fff" stroke-width="2"/></svg>
  <div class="rule" style="top:89px"></div>
  <nav class="nav"><span class="on">Home</span><span>About</span><span>Wholesale</span><span>Our Products</span><span>Services</span><span>Contact</span></nav>
  <div class="rule" style="top:138px"></div>
  <div class="hero-welcome head">Welcome to</div>
  <h1 class="hero-name head">HOLLOWPINE</h1>
  <div class="hero-sub head">SPIRITS</div>
  <p class="hero-copy">Turn your next drink idea into a reality and share your product with the world.<br>Hollowpine can bring your vision to life with our inhouse teams. We are here to help you through the entire process of creating unique spirit to compliment your brand. From formulating the recipe to production and even to helping you market your newest drink;</p>
  <div class="btn" style="left:505px;top:512px;width:190px;height:60px">Get Started</div>
</section>

<section class="about">
  <h2 class="head">About Hollowpine<br>Spirits</h2>
  <div class="about-copy">
    <p>Hollowpine Spirits, located in the Netherlands, has been mixing creating 5-star-rated gin, cocktails and making recipes since 2017. Now we want to use our distilling expertise to help you launch your very own brand of liquor.</p>
    <p style="margin-top:26px">Through our vast network we have exclusive access some of the best Whiskies, Vodka, Rum, Gins and Wines in the world.<br>We work directly with you to develop the perfect recipe and produce your drink</p>
  </div>
  <div class="btn" style="left:111px;top:438px;width:192px;height:52px">Learn More</div>
  <div class="about-photo" role="img" aria-label="Amber spirit bottle with splashing liquid inside a gold ring"></div>
</section>

<section class="wholesale">
  <h2 class="title head" style="top:80px">Wholesale</h2>
  <p class="wholesale-copy">We have exclusive access to spirits from world-class distilleries globally producing award winning We are able to supply large volumes of high-end spirit world-wide if you wish to bottle in your own facility.</p>
  <div class="tiles">
    <div class="tile" role="img" aria-label="Whisky poured over ice" style="background:linear-gradient(135deg,#1a0f08,#6b3a14 60%,#2a180a)">Whiskies</div>
    <div class="tile" role="img" aria-label="Vodka shots in blue light" style="background:linear-gradient(135deg,#0a2a6a,#1f6fd0 55%,#06163a)">Vodka</div>
    <div class="tile" role="img" aria-label="Rum bottle by a tropical lagoon" style="background:linear-gradient(135deg,#3a3414,#8a7a3a 50%,#2a1a0a)">Rum</div>
    <div class="tile" role="img" aria-label="Gin bottle with lemons and herbs" style="background:linear-gradient(135deg,#3a4a24,#6a6a40 50%,#2a2a18)">Gins</div>
    <div class="tile" role="img" aria-label="Row of wine bottles in a crate" style="background:linear-gradient(135deg,#2a2418,#8a7a60 50%,#1a140c)">Wines</div>
    <div class="tile" role="img" aria-label="Champagne bottle with cork" style="background:linear-gradient(135deg,#2a2420,#5a4a3a 50%,#141010)">Champagnes</div>
  </div>
</section>

<section class="services">
  <div class="svc-floor" role="img" aria-label="Dark wooden floor boards"></div>
  <div class="svc-photo" role="img" aria-label="Champagne flutes, whisky glass and bottles standing on the floor"></div>
  <h2 class="title head" style="top:80px">Our Services</h2>
  <svg class="abs" style="left:0;top:0" width="1200" height="644" viewBox="0 0 1200 644">
    <path d="M326 620 Q328 440 370 340 Q420 250 507 229 L678 229 Q780 250 826 340 Q872 440 874 620" fill="none" stroke="#ffc400" stroke-width="1.5" stroke-dasharray="5 5"/>
  </svg>
  <div class="svc-icon" style="left:461px;top:183px"><svg width="40" height="36" viewBox="0 0 40 36" fill="none" stroke="#ffc400" stroke-width="2"><rect x="2" y="4" width="36" height="28"/><path d="M2 13h36M2 22h36M11 4v28M20 4v28M29 4v28"/></svg></div>
  <div class="svc-icon" style="left:632px;top:183px"><svg width="40" height="40" viewBox="0 0 40 40" fill="none" stroke="#ffc400" stroke-width="2"><path d="M8 14h10v6a5 5 0 0 1-10 0z M13 25v10M9 35h8"/><path d="M26 6h6v6l3 4v20H23V16l3-4z"/></svg></div>
  <div class="svc-icon" style="left:324px;top:294px"><svg width="40" height="40" viewBox="0 0 40 40" fill="none" stroke="#ffc400" stroke-width="2"><circle cx="20" cy="20" r="16" stroke-dasharray="4 3"/><circle cx="20" cy="20" r="7"/></svg></div>
  <div class="svc-icon" style="left:780px;top:294px"><svg width="30" height="40" viewBox="0 0 30 40" fill="none" stroke="#ffc400" stroke-width="2"><rect x="5" y="4" width="20" height="32" rx="3"/><path d="M5 10h20M5 30h20"/></svg></div>
  <div class="svc-icon" style="left:288px;top:442px"><svg width="32" height="40" viewBox="0 0 32 40" fill="none" stroke="#ffc400" stroke-width="2"><rect x="3" y="3" width="26" height="34" rx="2"/><path d="M9 12h14M9 19h14M9 26h9"/></svg></div>
  <div class="svc-icon" style="left:833px;top:442px"><svg width="40" height="40" viewBox="0 0 40 40" fill="none" stroke="#ffc400" stroke-width="2"><circle cx="20" cy="18" r="12"/><path d="M13 28l-3 9 10-4 10 4-3-9"/></svg></div>

  <div class="svc r" style="left:212px;top:150px"><h3 class="head">Concept to Shelf</h3><p>Our team assists you through the entire<br>drink-making process.We consistently<br>meet with you</p><a>LEARN MORE</a></div>
  <div class="svc" style="left:750px;top:168px"><h3 class="head">Small Batch &amp; Spirit Bottling</h3><p>As a fully operational distillery, we can<br>continue to produce small batches of</p><a>LEARN MORE</a></div>
  <div class="svc r" style="left:70px;top:290px"><h3 class="head">Trial Production</h3><p>With your drink recipe ready, it's time to<br>start production. We begin by producing<br>a test batch of your drink</p><a>LEARN MORE</a></div>
  <div class="svc" style="left:894px;top:290px"><h3 class="head">Canning Services</h3><p>We now offer canning services for<br>things like ready-made drinks in various<br>sizes. You can ask our team about the</p><a>LEARN MORE</a></div>
  <div class="svc r" style="left:34px;top:440px"><h3 class="head">Recipe Development</h3><p>Our team works with you to perfect your<br>drink recipe to deliver the exact taste<br>you're looking for.</p><a>LEARN MORE</a></div>
  <div class="svc" style="left:942px;top:440px"><h3 class="head">Branding</h3><p>We can help create a branding and<br>marketing plan for your new product<br>based on your target demographic to</p><a>LEARN MORE</a></div>
</section>

<section class="faq">
  <h2 class="title head" style="top:85px">Frequently Asked Questions</h2>
  <div class="faq-item" style="top:188px"><span class="faq-num">01</span><span class="faq-q head">Where is Hollowpine Spirits based?</span><span class="faq-toggle">+</span></div>
  <div class="faq-item" style="top:291px"><span class="faq-num">02</span><span class="faq-q head">What if I am outside of the Netherlands? Can you still create my drink?</span><span class="faq-toggle">+</span></div>
  <div class="faq-item" style="top:395px"><span class="faq-num">03</span><span class="faq-q head">Is it required to have experience in the beverage industry to make a drink?</span><span class="faq-toggle">+</span></div>
  <div class="faq-item open" style="top:494px"><span class="faq-num">04</span><span class="faq-q head">What types of marketing and branding do you offer?</span><span class="faq-toggle">–</span></div>
  <div class="faq-answer">
    <p>In meetings with our team, we will help you workshop the perfect branding plan to help get your product in front of the consumers' eyes in the best way possible. We can assist you with everything from logo design to a marketing plan.</p>
    <p style="margin-top:26px">Branding is arguably the most significant part of the process. You can make the best-tasting drink in the world, but people will only know that if they can find it.</p>
  </div>
  <div class="faq-item" style="top:760px;left:221px"><span class="faq-num">05</span><span class="faq-q head">Can your team help me meet the legal requirements for selling alcohol?</span><span class="faq-toggle">+</span></div>
  <div class="faq-item" style="top:863px;left:221px"><span class="faq-num">06</span><span class="faq-q head">What drinks can Hollowpine Spirits help me create?</span><span class="faq-toggle">+</span></div>
</section>

<section class="contact">
  <h2 class="title head" style="top:85px">Contact Us</h2>
  <div class="info" style="top:163px"><span class="info-icon"><svg width="16" height="20" viewBox="0 0 14 16"><path d="M7 1a5 5 0 0 1 5 5c0 4-5 9-5 9S2 10 2 6a5 5 0 0 1 5-5z" fill="none" stroke="#fff" stroke-width="1.5"/><circle cx="7" cy="6" r="1.8" fill="#fff"/></svg></span><div><h4 class="head">Location</h4><p>Hollowpine Spirits Building 12, Harbour Lane 4, Eastmoor, 4821 KD</p></div></div>
  <div class="info" style="top:290px"><span class="info-icon"><svg width="18" height="18" viewBox="0 0 14 14"><path d="M3 1l3 3-2 2c1 2 2 3 4 4l2-2 3 3-2 2C6 13 1 8 1 3z" fill="#fff"/></svg></span><div><h4 class="head">Phone</h4><p>+31600000123</p></div></div>
  <div class="info" style="top:368px"><span class="info-icon"><svg width="18" height="14" viewBox="0 0 18 14"><rect x="1" y="1" width="16" height="12" rx="1" fill="#fff"/><path d="M1 2l8 6 8-6" stroke="#121212" stroke-width="1.5" fill="none"/></svg></span><div><h4 class="head">Email</h4><p>info@hollowpinespirits.com</p></div></div>
  <div class="field" style="left:433px;top:170px">First Name</div>
  <div class="field" style="left:769px;top:170px">Last Name</div>
  <div class="field" style="left:433px;top:238px">Company</div>
  <div class="field" style="left:769px;top:238px">Telephone</div>
  <div class="field" style="left:433px;top:306px">Email</div>
  <div class="field" style="left:769px;top:306px;height:124px">Message</div>
  <div class="btn" style="left:433px;top:375px;width:318px;height:52px;border-radius:0">Submit</div>
</section>

<footer class="footer">
  <div class="brand" style="left:111px;top:78px;width:290px;font-size:30px;text-align:left">HOLLOWPINE<div style="font-size:11px;letter-spacing:12px;margin-top:8px">SPIRITS</div></div>
  <p class="abs" style="left:111px;top:162px;width:280px;font-size:14px;line-height:24px">Lorem ipsum dolor sit amet, consectetur adipiscing elit, sed do eiusmod tempor incididunt ut labore</p>
  <h4 class="foot-h head" style="left:457px">Quick Links</h4>
  <ul class="foot-list" style="left:457px"><li>›&nbsp; <span style="color:var(--gold)">Home</span></li><li>›&nbsp; About</li><li>›&nbsp; Wholesale</li><li>›&nbsp; Our Products</li><li>›&nbsp; Services</li><li>›&nbsp; Contact</li></ul>
  <h4 class="foot-h head" style="left:655px">Follow Us</h4>
  <ul class="foot-list" style="left:655px"><li>▪&nbsp; Pinewire</li><li>▪&nbsp; Reelbox</li><li>▪&nbsp; Circlefeed</li><li>▪&nbsp; Snapframe</li><li>▪&nbsp; Chirpline</li></ul>
  <h4 class="foot-h head" style="left:845px">Newsletter Updates</h4>
  <p class="abs" style="left:848px;top:103px;font-size:13.5px">Name*</p>
  <div class="foot-line" style="top:130px"></div>
  <p class="abs" style="left:848px;top:155px;font-size:13.5px">Email*</p>
  <div class="foot-line" style="top:180px"></div>
  <div class="btn" style="left:841px;top:215px;width:173px;height:40px">Submit Now</div>
</footer>
<p class="copyright">©Copyrights 2022 &nbsp;<span style="color:var(--gold)">Hollowpine Spirits</span>&nbsp; All Rights Reserved</p>

</body>
</html>
```